Pella Acupuncture Business Card Design

I would like a business card design for my acupuncture business which is based from 2 practices in Melbourne, Australia.

The front of the card should include:

*The Logo
* Name - Miranda Tovelisca (B.App.Sc.(TCM), Dip.Rem.Mass.). (I would like the letters after my name in slightly smaller font)
* Mobile number - 0472 318 604
* Web address - www.pellaacupuncture-example.com.au

On the back of the card I would somehow like to fit my 2 clinic addresses in. They are:

The Birchwood Restoration Rooms
842 Fennimore Rd, Camberwell VIC 3124
Ph: 1300 274 518

Quillbrook Integrative & Eastern Herbal Therapy Clinic
31 Marlowby Rd, Malvern East VIC 3145
Ph: (03) 9871 3352

If there is space, I'd also like to add to the back of the card - Next Appointment............................ (or something along those lines).

Thanks and happy designing!

Target Market(s)

Health consumers, and colleagues in the health industry

Industry/Entity Type

Clinic

Contact Information for Business Card

as above in brief

Requirements
Must have
• I've seen some ok designs coming in, however I'd like to avoid the generic look with the added curved line details etc. I don't particularly need extra patterns added to the card. I'd prefer it to look quite clean and simple, and using more earthy colours (I'm not super keen on the lime green that a lot of designs seem to include. I don't mind the full black or white look, (obviously the back side needs to be a lighter colour to allow me to write appointment details on it). I also quite like the idea of the background looking like brown recycled paper (just an idea - that's not 100% necessary).
Nice to have
• I have an idea that I could have the main flower part of the logo printed as metallic.
Should not have
• Generic patterns and too much added detail.

```html
<!DOCTYPE html>
<html lang="en">
<head>
<meta charset="utf-8">
<title>Pella Acupuncture – Business Card</title>
<link rel="stylesheet" href="https://fonts.googleapis.com/css2?family=Alegreya:wght@400;500&display=swap">
<style>
  :root {
    --stage: #e9e6e1;
    --card-black: #0d0c0b;
    --card-paper: #f8f4ec;
    --accent-bronze: #b39462;
    --accent-earth: #7a6440;
    --soft-grey: #9c958b;
    --ink-grey: #847c70;
    --text-white: #f2efe9;
    --rule: #d3c9b8;
    --panel: #eee7da;
    --panel-edge: #e0d7c6;
    --deco-dark: #2e2a26;
    --serif: "Alegreya", Georgia, serif;
  }
  * { box-sizing: border-box; margin: 0; padding: 0; }
  html, body { width: 1200px; height: 1000px; overflow: hidden; }
  body { background: var(--stage); font-family: var(--serif); position: relative; }

  .card {
    position: absolute;
    left: 250px;
    width: 700px;
    height: 400px;
    overflow: hidden;
    box-shadow: 0 6px 18px rgba(0,0,0,0.18);
  }

  /* Front */
  .card-front { top: 60px; background: var(--card-black); }
  .front-deco {
    position: absolute;
    left: 300px; top: 170px;
    width: 420px; height: 420px;
    border-radius: 50%;
    background: radial-gradient(circle, #3a3530 0%, var(--deco-dark) 55%, rgba(46,42,38,0) 72%);
  }
  .brand {
    position: absolute;
    left: 56px; top: 48px;
    display: flex; align-items: center; gap: 16px;
  }
  .brand-dot { width: 64px; height: 64px; border-radius: 50%; background: var(--accent-bronze); }
  .brand-name { color: var(--accent-bronze); font-size: 24px; font-weight: 400; letter-spacing: 0.04em; }
  .practitioner {
    position: absolute;
    left: 56px; top: 150px;
    color: var(--text-white);
  }
  .practitioner-name { font-size: 46px; font-weight: 400; line-height: 1; }
  .practitioner-name .surname { color: var(--accent-bronze); }
  .credentials {
    margin-top: 10px;
    font-size: 22px; color: var(--soft-grey);
    font-variant: small-caps; letter-spacing: 0.03em;
  }
  .front-contact {
    position: absolute;
    left: 56px; top: 290px;
    color: var(--accent-bronze); font-size: 22px; line-height: 1.5;
  }
  .front-contact .label { display: inline-block; width: 90px; }

  /* Back */
  .card-back { top: 540px; background: var(--card-paper); display: flex; }
  .clinics { width: 400px; border-right: 2px solid var(--rule); display: flex; flex-direction: column; }
  .clinic { flex: 1; padding: 32px 36px; }
  .clinic + .clinic { border-top: 2px solid var(--rule); }
  .clinic-name { color: var(--accent-earth); font-size: 21px; font-weight: 500; line-height: 1.2; margin-bottom: 10px; }
  .clinic-address { color: var(--ink-grey); font-size: 16px; line-height: 1.4; font-style: normal; }
  .appointment { flex: 1; padding: 32px 30px; display: flex; flex-direction: column; align-items: center; }
  .appointment-title { color: var(--accent-earth); font-size: 24px; font-weight: 400; text-align: center; line-height: 1.2; margin-bottom: 18px; }
  .appointment-box {
    width: 100%; flex: 1;
    background: var(--panel);
    border: 1px solid var(--panel-edge);
    padding: 26px 24px;
    display: flex; flex-direction: column; justify-content: space-around;
  }
  .write-line { border-bottom: 2px dashed var(--rule); height: 1px; }
</style>
</head>
<body>

  <section class="card card-front" aria-label="Business card front">
    <div class="front-deco" role="img" aria-label="Large faint flower decoration"></div>
    <div class="brand">
      <span class="brand-dot"></span>
      <span class="brand-name">Pella Acupuncture</span>
    </div>
    <div class="practitioner">
      <h1 class="practitioner-name">Miranda <span class="surname">Tovelisca</span></h1>
      <p class="credentials">B.App.Sc.(TCM), Dip.Rem.Mass.</p>
    </div>
    <div class="front-contact">
      <p><span class="label">Mobile</span>0472 318 604</p>
      <p>www.pellaacupuncture-example.com.au</p>
    </div>
  </section>

  <section class="card card-back" aria-label="Business card back">
    <div class="clinics">
      <div class="clinic">
        <h2 class="clinic-name">The Birchwood Restoration Rooms</h2>
        <address class="clinic-address">842 Fennimore Rd<br>Camberwell VIC 3124<br>Ph. 1300 274 518</address>
      </div>
      <div class="clinic">
        <h2 class="clinic-name">Quillbrook Integrative &amp; Eastern Herbal Therapy Clinic</h2>
        <address class="clinic-address">31 Marlowby Rd<br>Malvern East VIC 3145<br>Ph. (03) 9871 3352</address>
      </div>
    </div>
    <div class="appointment">
      <h2 class="appointment-title">Next<br>Appointment</h2>
      <div class="appointment-box">
        <div class="write-line"></div>
        <div class="write-line"></div>
        <div class="write-line"></div>
      </div>
    </div>
  </section>

</body>
</html>
```